Design an Outstanding flyer for my company.

I need a flyer designed for our window tinting company based in Brisbane Queensland Australia. The flyer will be targeting Home tinting. We also do mobile car tinting. Something in regards to this could be incorporated into the flyer as well.
I want it to be 2 sided DL size. Black background.
It really needs to Pop, and be a real attention getter.
It needs to be easy to read.
I have provided a mock up with the info on it from our marketing company. It will need a spellcheck etc to make sure everything is correct.
Everything about it can be changed however you like.
I have also included the company logo.

Lets see what you've got!

Target Market(s)

Home Owners

Industry/Entity Type

Home Improvement

Font styles to use
Other font styles liked:
• Duan Penh

Requirements
Must have
• All the information on the mock up. Clear and easy to read.
• Must Stand Out!

```html
<!DOCTYPE html>
<html lang="en">
<head>
<meta charset="utf-8">
<title>BrightPeak Window Tinting – Home Tinting Flyer</title>
<link rel="stylesheet" href="https://fonts.googleapis.com/css2?family=Arimo:wght@700&family=Roboto+Condensed:wght@400;500;700&family=Open+Sans:wght@400;600&display=swap">
<style>
  :root {
    --page: #ffffff;
    --black: #000000;
    --panel: #111111;
    --panel-mid: #1c1c1c;
    --yellow: #ffee00;
    --gold: #f8c400;
    --gold-deep: #b68a1a;
    --white: #ffffff;
    --steel: #8c8c8c;
    --ink: #1a1a1a;
  }
  * { margin: 0; padding: 0; box-sizing: border-box; }
  html, body { width: 996px; height: 1200px; overflow: hidden; background: var(--page); }
  .canvas { position: relative; width: 996px; height: 1200px; }

  .flyer { position: absolute; left: 264px; top: 144px; width: 454px; height: 872px; background: linear-gradient(180deg, var(--panel) 0%, var(--panel-mid) 50%, var(--panel) 100%); overflow: hidden; }

  .headline-block { position: absolute; left: 2px; top: 0; width: 452px; height: 291px; background: var(--black); text-align: center; font-family: "Arimo", Arial, sans-serif; font-weight: 700; line-height: 1; }
  .headline-block p { position: absolute; left: 0; width: 100%; }
  .h-heat { top: 42px; font-size: 48px; color: var(--white); }
  .h-uv { top: 100px; font-size: 33px; color: var(--yellow); }
  .h-money { top: 142px; font-size: 62px; color: var(--white); }
  .h-privacy { top: 213px; font-size: 39px; color: var(--yellow); }

  .gold-accent { position: absolute; left: 0; top: 390px; }

  .benefits { position: absolute; left: 42px; top: 270px; width: 370px; text-align: center; font-family: "Roboto Condensed", Arial Narrow, sans-serif; font-size: 12.3px; line-height: 17.4px; color: var(--white); text-transform: uppercase; }

  .reasons { position: absolute; left: 0; top: 423px; width: 100%; text-align: center; font-family: "Roboto Condensed", Arial Narrow, sans-serif; font-weight: 500; font-size: 27px; line-height: 31.5px; color: var(--yellow); }

  .call-band { position: absolute; left: 0; top: 532px; width: 100%; height: 184px; background: linear-gradient(180deg, var(--black), #171717 50%, var(--black)); border-top: 6px solid var(--gold); border-bottom: 6px solid var(--gold); text-align: center; font-family: "Roboto Condensed", Arial Narrow, sans-serif; font-weight: 700; color: var(--white); }
  .call-lead { margin-top: 14px; font-size: 28px; line-height: 35px; }
  .call-numbers { margin-top: 10px; font-size: 32px; line-height: 38px; }

  .brand-area { position: absolute; left: 0; top: 716px; width: 100%; height: 123px; }
  .brand-backdrop { position: absolute; inset: 0; background: radial-gradient(ellipse at 80% 40%, #9a9a9a 0%, #3a3a3a 45%, #111 80%); }
  .brand { position: absolute; left: 0; top: 34px; width: 100%; display: flex; align-items: center; justify-content: center; gap: 12px; font-family: "Arimo", Arial, sans-serif; font-weight: 700; font-size: 30px; color: var(--gold); }
  .brand-dot { width: 22px; height: 22px; border-radius: 50%; background: var(--gold); }

  .web-band { position: absolute; left: 0; bottom: 0; width: 100%; height: 33px; background: linear-gradient(90deg, var(--gold), var(--yellow) 50%, var(--gold)); text-align: center; font-family: "Open Sans", Arial, sans-serif; font-size: 16px; line-height: 33px; color: var(--ink); }
</style>
</head>
<body>
<main class="canvas">
  <article class="flyer">
    <svg class="gold-accent" width="120" height="150" viewBox="0 0 120 150" aria-hidden="true">
      <defs>
        <linearGradient id="goldShade" x1="0" y1="0" x2="1" y2="1">
          <stop offset="0" stop-color="#7a5a12"/>
          <stop offset="0.5" stop-color="#e2b52a"/>
          <stop offset="1" stop-color="#f5d44a"/>
        </linearGradient>
      </defs>
      <polygon points="0,10 0,142 96,142" fill="url(#goldShade)"/>
    </svg>

    <header class="headline-block">
      <p class="h-heat">KEEP HEAT OUT</p>
      <p class="h-uv">BLOCK 99.9% UV RAYS</p>
      <p class="h-money">SAVE MONEY</p>
      <p class="h-privacy">INCREASE PRIVACY</p>
    </header>

    <p class="benefits">Reduce glare. Reduce energy costs. Control the amount of light entering your home. Reduce carbon footprint. Make home more beautiful. Eliminate home hot spots. Protect against broken glass. Regulate energy. Protects upholstery. Improve effectiveness of roof insulation. Improve health. Reduces interior floor fading. Eliminate need for blinds. Strengthen your windows. Insulate in winter. Affoardable.</p>

    <p class="reasons">20 REASONS WHY<br>HOME WINDOW TINTING<br>IS PERFECT FOR YOU.</p>

    <section class="call-band">
      <p class="call-lead">CALL BRISBANE’S LEADER IN<br>HOME WINDOW TINTING NOW.</p>
      <p class="call-numbers">TEL 07 3000 1234<br>SMS: 0400 000 111</p>
    </section>

    <section class="brand-area">
      <div class="brand-backdrop" role="img" aria-label="Sweeping silver and white curved streaks on black behind the company name"></div>
      <p class="brand"><span class="brand-dot"></span>BrightPeak Window Tinting</p>
    </section>

    <footer class="web-band">www.brightpeaktinting.com.au</footer>
  </article>
</main>
</body>
</html>
```